brelvatrim.com

I have a site already disigned, however at the time I had no clue of how and what my site should look like. Still pretty cluless but I know I need to make some fundamenlal changes. I'm looking fora designer who understands how to connect with the cosumer with a ballance of visual and content with SEO in mind.I have a lot of content ready to be added to the mix, just missing alot of bottons for the content for example I have FAQ content but no FAQ botton. There are a lot of things I would like to add and take away from the current site. Here is a list of what I would like to add and subtracted from the site.Take away the find botton and ad contact us change the about botton to about brelvatrim,under that botton i want bottons that lead to News/Events,carreer opertunities,contact us and priacy policy. I also want to add Services offered: personal training,Motivational speeking ,bootcamp conditioning,rondalo,kickboxing cardio,and hip hop cordio. I want to add a botton for testimonials:video and written. I need to add a blog botton, a FAQ botton, and before and after. I want to add a social media botton: pagewall, snapreel,chirpline,pinlocal,clipstream,and spot hopper. I need to add a store botton; T shirts. I would like the contact info the be linked to my email. and I would like would like at the top of contact form to read Request a free info session Now!!! But I don't need a new design I need to add these thing to the one I already have whitch is CMS based

Reason: I need my site to have new logo, just figured out how to down load logo

Reason: I need site to be CMS based so I can up load content and pics

Target Market(s)

People who want to loose weight, mostley women over the age of 30 and men over the age of 40 that income is at least 60,000 a year

Industry/Entity Type

Store

Font styles to use
Sans Serif
Decorative

Colors
000000
ec1f27
0255a3

Requirements
Must have
• Adding the drop downs listed above

```html
<!DOCTYPE html>
<html lang="en">
<head>
<meta charset="utf-8">
<title>Brelvatrim — Changing Lifestyles</title>
<link rel="stylesheet" href="https://fonts.googleapis.com/css2?family=Roboto+Condensed:ital,wght@0,300;0,400;0,700;1,300;1,400&display=swap">
<style>
  :root {
    --red: #d4262b;
    --red-bright: #ec1f27;
    --red-deep: #b81f24;
    --red-veil: rgba(214, 38, 43, 0.82);
    --black: #1f1f1f;
    --black-soft: #262626;
    --field: #1a1a1a;
    --white: #ffffff;
    --grey-light: #eeeeee;
    --ink-light: #f3d9d9;
    --font: "Roboto Condensed", "Arial Narrow", sans-serif;
  }
  * { box-sizing: border-box; margin: 0; padding: 0; }
  html, body { width: 999px; height: 1200px; overflow: hidden; background: var(--red); }
  body { position: relative; font-family: var(--font); color: var(--white); }
  .abs { position: absolute; }

  /* Sidebar */
  .sidebar { left: 0; top: 0; width: 178px; height: 1200px; background: var(--red); }
  .brand { left: 0; top: 30px; width: 178px; height: 130px; }
  .brand-mark { position: absolute; left: 44px; top: 14px; width: 90px; height: 90px; border-radius: 50%; background: var(--black); }
  .brand-name { position: absolute; left: 0; top: 48px; width: 178px; text-align: center; font-size: 22px; font-weight: 700; letter-spacing: 0.5px; color: var(--white); }
  .nav { left: 0; top: 180px; width: 178px; list-style: none; }
  .nav li { height: 30px; line-height: 26px; text-align: center; font-size: 10px; text-transform: uppercase; }
  .nav li.is-active { background: var(--red-deep); }

  .info-form { left: 0; top: 421px; width: 178px; height: 239px; background: var(--black); }
  .info-form::before { content: ""; position: absolute; left: 82px; top: 0; border: 7px solid transparent; border-top-color: var(--red); }
  .info-form h2 { position: absolute; top: 12px; width: 178px; text-align: center; font-size: 10.5px; font-weight: 400; text-transform: uppercase; }
  .field { position: absolute; left: 17px; width: 145px; height: 20px; background: var(--field); font-size: 8.5px; line-height: 20px; padding-left: 11px; text-transform: uppercase; }
  .field.select::after { content: ""; position: absolute; right: 8px; top: 6px; width: 4px; height: 4px; border-right: 1px solid var(--white); border-bottom: 1px solid var(--white); transform: rotate(45deg); }
  .book-now { position: absolute; left: 16px; top: 195px; width: 143px; height: 25px; background: var(--red-bright); font-size: 13px; line-height: 25px; text-align: center; text-transform: uppercase; }

  .follow { left: 0; top: 660px; width: 178px; height: 80px; background: var(--red-bright); text-align: center; }
  .follow h3 { font-size: 9.5px; font-weight: 400; margin-top: 13px; text-transform: uppercase; }
  .social { margin-top: 6px; font-size: 8px; line-height: 11px; }
  .legal { left: 0; top: 746px; width: 178px; text-align: center; font-size: 7px; line-height: 23px; text-transform: uppercase; }

  /* Hero */
  .hero-photo { left: 178px; top: 0; width: 821px; height: 740px;
    background: linear-gradient(160deg, #8f6a60 0%, #5c4a48 30%, #3a3030 55%, #7d5b48 100%); }
  .hero-next { left: 945px; top: 308px; }
  .headline { right: 116px; top: 104px; background: var(--black); font-size: 40px; font-weight: 400; line-height: 44px; padding: 0 3px; text-transform: uppercase; }
  .subline { right: 116px; top: 152px; background: var(--red-bright); font-size: 25px; line-height: 37px; padding: 0 8px; text-transform: uppercase; }

  /* Services */
  .services { left: 178px; top: 421px; width: 821px; height: 239px; background: var(--red-veil); }
  .services h2 { position: absolute; top: 24px; width: 821px; text-align: center; font-size: 24px; font-weight: 400; text-transform: uppercase; }
  .service { position: absolute; top: 66px; width: 120px; }
  .service-icon { width: 104px; height: 104px; border-radius: 50%; background: var(--black); display: flex; align-items: center; justify-content: center; }
  .service-name { margin: 13px 0 0 10px; font-size: 12px; line-height: 15px; text-transform: uppercase; color: var(--ink-light); }

  /* Blog */
  .blog-head { left: 178px; top: 740px; width: 482px; height: 53px; background: var(--red); font-size: 24px; line-height: 53px; padding-left: 29px; text-transform: uppercase; }
  .blog-body { left: 178px; top: 793px; width: 482px; height: 240px; background: var(--black-soft); }
  .post { position: absolute; left: 29px; width: 430px; }
  .post-thumb { position: absolute; left: 0; top: 0; width: 64px; height: 66px; border: 2px solid var(--white); }
  .post h4 { position: absolute; left: 93px; top: 2px; color: var(--red-bright); font-size: 14px; font-weight: 700; }
  .post p { position: absolute; left: 93px; top: 21px; width: 345px; font-size: 12px; line-height: 15px; font-style: italic; font-weight: 300; }

  /* Before / after */
  .ba-head { top: 740px; height: 53px; background: var(--black); font-size: 24px; line-height: 53px; padding-left: 24px; text-transform: uppercase; }
  .ba-head em { font-weight: 300; }
  .ba-photo { top: 793px; height: 240px; }

  /* Store */
  .store { left: 178px; top: 1033px; width: 821px; height: 167px; background: linear-gradient(90deg, #b8393a 0%, #c9474a 40%, #c24144 70%, #a83032 100%); }
  .store-link { left: 508px; top: 1098px; font-size: 27px; font-style: italic; font-weight: 300; letter-spacing: 1px; border-bottom: 1px solid var(--white); line-height: 30px; text-transform: uppercase; }
</style>
</head>
<body>

<aside class="abs sidebar">
  <div class="abs brand">
    <span class="brand-mark"></span>
    <span class="brand-name">brelvatrim</span>
  </div>

  <ul class="abs nav">
    <li class="is-active">Home</li>
    <li>About Brelvatrim</li>
    <li>Gallery</li>
    <li>News/Events</li>
    <li>Carreer Opertunities</li>
    <li>Training</li>
    <li>Contact Us</li>
  </ul>

  <form class="abs info-form">
    <h2>Request a free info session now</h2>
    <div class="field select" style="top:38px">Choose program</div>
    <div class="field" style="top:61px">Date</div>
    <div class="field select" style="top:84px">Number of persons</div>
    <div class="field" style="top:107px">E-mail</div>
    <div class="field" style="top:130px">Phone number</div>
    <div class="field" style="top:152px;height:37px;line-height:20px">Message</div>
    <div class="book-now">Book now</div>
  </form>

  <div class="abs follow">
    <h3>Follow us</h3>
    <p class="social">snapreel · pagewall · chirpline<br>pinlocal · clipstream · spot hopper</p>
  </div>

  <p class="abs legal">Brelvatrim. © 2014. Privacy policy<br>Blog</p>
</aside>

<div class="abs hero-photo" role="img" aria-label="Trainer and client doing a floor workout in the gym"></div>
<h1 class="abs headline">Changing lifestyles</h1>
<p class="abs subline">One heart rate at a time</p>
<svg class="abs hero-next" width="54" height="108" viewBox="0 0 54 108" aria-hidden="true">
  <polygon points="54,0 54,108 0,54" fill="var(--red-bright)"/>
  <polyline points="31,46 39,54 31,62" fill="none" stroke="#fff" stroke-width="2"/>
</svg>

<section class="abs services">
  <h2>Our services</h2>

  <div class="service" style="left:20px">
    <div class="service-icon">
      <svg width="44" height="44" viewBox="0 0 44 44"><circle cx="18" cy="8" r="5" fill="#fff"/><rect x="11" y="15" width="14" height="27" rx="3" fill="#fff"/><rect x="30" y="20" width="10" height="3" fill="var(--red-bright)"/><rect x="30" y="27" width="10" height="3" fill="var(--red-bright)"/><rect x="33.5" y="17" width="3" height="9" fill="var(--red-bright)"/></svg>
    </div>
    <p class="service-name">Personal<br>training</p>
  </div>

  <div class="service" style="left:152px">
    <div class="service-icon">
      <svg width="40" height="48" viewBox="0 0 40 48"><polygon points="10,2 18,2 22,22 16,22" fill="#fff"/><polygon points="30,2 22,2 18,22 24,22" fill="#fff"/><circle cx="20" cy="34" r="11" fill="#fff"/><circle cx="20" cy="34" r="5" fill="var(--red-bright)"/></svg>
    </div>
    <p class="service-name">Motivational<br>speeking</p>
  </div>

  <div class="service" style="left:284px">
    <div class="service-icon">
      <svg width="64" height="44" viewBox="0 0 64 44"><rect x="2" y="20" width="60" height="3" fill="#fff"/><rect x="6" y="12" width="5" height="19" fill="var(--red-bright)"/><rect x="12" y="9" width="5" height="25" fill="#fff"/><rect x="47" y="9" width="5" height="25" fill="#fff"/><rect x="53" y="12" width="5" height="19" fill="var(--red-bright)"/><circle cx="32" cy="6" r="5" fill="#fff"/><rect x="26" y="13" width="12" height="30" rx="3" fill="#fff"/></svg>
    </div>
    <p class="service-name">Bootcamp<br>conditioning</p>
  </div>

  <div class="service" style="left:416px">
    <div class="service-icon">
      <svg width="44" height="50" viewBox="0 0 44 50"><circle cx="26" cy="6" r="5" fill="#fff"/><polyline points="24,14 20,30 30,38 30,48" fill="none" stroke="#fff" stroke-width="6" stroke-linejoin="round"/><polyline points="20,30 10,36 6,46" fill="none" stroke="var(--red-bright)" stroke-width="6" stroke-linejoin="round"/><polyline points="24,17 14,24" fill="none" stroke="#fff" stroke-width="4"/></svg>
    </div>
    <p class="service-name">Rondalo</p>
  </div>

  <div class="service" style="left:548px">
    <div class="service-icon">
      <svg width="46" height="50" viewBox="0 0 46 50"><rect x="19" y="1" width="8" height="5" fill="#fff"/><circle cx="23" cy="28" r="18" fill="none" stroke="#fff" stroke-width="6"/><line x1="23" y1="28" x2="31" y2="20" stroke="var(--red-bright)" stroke-width="4"/><line x1="38" y1="9" x2="42" y2="13" stroke="#fff" stroke-width="4"/></svg>
    </div>
    <p class="service-name">Kickboxing<br>cardio</p>
  </div>

  <div class="service" style="left:679px">
    <div class="service-icon">
      <svg width="48" height="44" viewBox="0 0 48 44"><path d="M24 42 L5 23 A11 11 0 0 1 24 8 A11 11 0 0 1 43 23 Z" fill="#fff"/><polyline points="4,22 16,22 20,14 25,30 29,20 44,20" fill="none" stroke="var(--red-bright)" stroke-width="3"/></svg>
    </div>
    <p class="service-name">Hip hop<br>cardio</p>
  </div>
</section>

<h2 class="abs blog-head">Blog posts</h2>
<section class="abs blog-body">
  <article class="post" style="top:34px">
    <div class="post-thumb" role="img" aria-label="Trainer coaching a client in the gym" style="background:linear-gradient(135deg,#6b6b6b,#2d2d2d)"></div>
    <h4>Amet, consectetuer adipiscing elit</h4>
    <p>Lorem ipsum dolor sit amet, consectetuer adipiscing elit, sed diam nonummy nibh euismod tincidunt ut laoreet dolore magna aliquam erat volutpat. Ut wisi enim ad minim veniam, quis nostrud exerci tation.</p>
  </article>
  <article class="post" style="top:135px">
    <div class="post-thumb" role="img" aria-label="Woman working out with weights" style="background:linear-gradient(135deg,#c9d6e0,#c2607a)"></div>
    <h4>Amet, consectetuer adipiscing elit</h4>
    <p>Lorem ipsum dolor sit amet, consectetuer adipiscing elit, sed diam nonummy nibh euismod tincidunt ut laoreet dolore magna aliquam erat volutpat. Ut wisi enim ad minim veniam, quis nostrud exerci tation.</p>
  </article>
</section>

<h2 class="abs ba-head" style="left:660px;width:143px">Before</h2>
<h2 class="abs ba-head" style="left:803px;width:196px;padding-left:12px">After <em>Brelvatrim</em></h2>
<div class="abs ba-photo" role="img" aria-label="Client before the program, side view" style="left:660px;width:143px;background:linear-gradient(180deg,#ffffff,#f2ece8)"></div>
<div class="abs ba-photo" role="img" aria-label="Client after the program, side view" style="left:803px;width:196px;background:linear-gradient(180deg,var(--grey-light),#e6e0dc)"></div>

<section class="abs store" role="img" aria-label="Store banner with training apparel, gloves and shorts"></section>
<p class="abs store-link">Visit store</p>

</body>
</html>
```